Looking for Landingpage / Website Designer

We are looking for a Web Designer / Developer for our upcoming Start Up Websites. The first project will be a simple responsive business website with a CTA- Button and an optional Newsletter Opt-In. We do aim for a modern online business approach, since we are a young company.

It is necessary to understand, that we need a conversion orientated design, not a wordpress blog with widgets and galleries.

We are currently discussing how it is going to happen and what preferences we need to focus on.

What we know is, that it should be more of a landing page with an option of adding 2 or 3 Navigation points.

We even thought about using services like pagemarlo.com or formvista.com to have an easier approach for future customizations and A/B testing.

We'd love to see how you fit the design/colors to the upcoming logo
(which is not the final version yet )

hope you can do something about that.

For the Structure.

1. Bracket

Slogan plus a preview text of what we are offering. On the right side a video placeholder plus CTA button.

2. Bracket

Illustrating 3 Benefits. On the right side - Opt in for Contact/Newsletter and CTA Button

3. Bracket

Picture with text just like you have it with the testimonial

You can orientate yourself towards to that landing page example as well:

http://cdn2.quentarix.net/hub/53/file-581676469-png/Blog-Related_Images/pagemarlo_landing_page.png?t=1416543075530

If our collaboration is going well, we would like to stay in touch for further projects.

Reason: There are 3 Design we do really like but, don't fit exactly our needs. 5 Days max.

Reason: For final adjustments.

I just uploaded the final logo :) Thank you for your commitment so far!

Target Market(s)

Our targeted audience could be almost everybody, who looks for an average paid side job (students, unemployed, house wives and whatever you can imagine). Maybe this is enough information for you to get a mere perception of what this is all about.

Industry/Entity Type

Business

Coding

Coded - Design and coding required

Font styles to use
Serif
Sans Serif

Colors
acd037
5c5c5c
33a6d7

Requirements
Must have
• Registration Opt-In
Responsive on any Device
Customizable
A benefits navigation just like in that example I've uploaded.
Nice to have
• As fast as possible ;D

```html
<!DOCTYPE html>
<html lang="en">
<head>
<meta charset="utf-8">
<title>Sidework Hub</title>
<link href="https://fonts.googleapis.com/css2?family=Lato:ital,wght@0,400;0,700;0,900;1,400;1,700&display=swap" rel="stylesheet">
<style>
:root{
  --black:#000;
  --green:#52b747;
  --green-dark:#2f8f1f;
  --hero:#96d48a;
  --card:#3a3536;
  --nav-active:#8a8878;
  --arrow:#4a4a44;
  --grey-band:#e3e3e3;
  --text-dark:#444;
  --white:#fff;
}
*{box-sizing:border-box;margin:0;padding:0}
html,body{width:1024px;height:1200px;overflow:hidden}
body{font-family:'Lato',sans-serif;background:var(--white);position:relative;color:var(--text-dark)}
.abs{position:absolute}
.site-header{left:0;top:0;width:1024px;height:86px;background:var(--black)}
.brand{left:142px;top:0;height:86px;display:flex;align-items:center}
.brand-name{font-size:34px;font-weight:700;color:var(--white);letter-spacing:.5px}
.main-nav{left:532px;top:0;height:86px;display:flex}
.main-nav a{display:flex;align-items:center;padding:0 8px;height:86px;color:var(--white);font-size:14px;font-weight:700;text-decoration:none}
.main-nav a.active{background:var(--nav-active)}
.hero{left:0;top:86px;width:1024px;height:386px;background:var(--hero)}
.hero-title{left:134px;top:150px;font-size:56px;font-weight:700;color:var(--white);line-height:1}
.hero-text{left:134px;top:222px;width:366px;font-size:13.6px;font-weight:700;line-height:20.8px;color:var(--white);text-align:justify}
.cta{left:136px;top:354px;width:157px;height:36px;background:var(--white);border-radius:3px;display:flex;align-items:center;justify-content:center;color:var(--green);font-style:italic;font-weight:700;font-size:18px}
.video{left:519px;top:157px;width:369px;height:234px;background:var(--white);padding:6px}
.video-screen{width:100%;height:100%;background:radial-gradient(circle at 50% 45%,#8e8f92,#3a3b3e 70%,#1d1d1f);position:relative}
.video-bar{position:absolute;left:0;right:0;bottom:0;height:20px;background:#111}
.video-progress{position:absolute;left:0;right:0;top:0;height:3px;background:#444}
.video-progress span{display:block;width:23%;height:3px;background:#d11}
.slide-arrow{top:262px;width:36px;height:35px;background:var(--arrow);color:var(--green);display:flex;align-items:center;justify-content:center}
.benefit,.signup{top:508px;width:177px;height:233px;background:var(--card);border-radius:2px;text-align:center;color:var(--white)}
.benefit-icon{margin:16px auto 0;width:84px;height:76px;background:var(--green);border:2px solid #e8e8e8;border-radius:3px;display:flex;align-items:center;justify-content:center}
.benefit h3{margin-top:14px;font-size:13.5px;font-weight:700}
.benefit p{margin-top:9px;font-size:10.4px;line-height:13.6px;padding:0 1px}
.btn{display:inline-flex;align-items:center;justify-content:center;height:28px;background:var(--green);color:var(--white);font-weight:700;font-style:italic;font-size:14px;border-radius:2px;letter-spacing:-.3px}
.benefit .btn{position:absolute;left:45px;top:192px;width:86px}
.signup h3{margin-top:12px;font-size:15px;font-weight:700}
.signup .field{margin:11px auto 0;width:157px;height:28px;background:var(--white);border-radius:2px;text-align:left;padding-left:7px;line-height:28px;font-size:11.5px;font-style:italic;color:#777}
.signup .field+.field{margin-top:7px}
.signup .btn{position:absolute;left:47px;top:192px;width:86px}
.reviews{left:0;top:783px;width:1024px;height:374px;background:var(--grey-band)}
.reviews-title{left:137px;top:801px;font-size:19px;font-style:italic;font-weight:700;color:var(--text-dark)}
.reviewer{font-size:14px;color:#555}
.reviewer b{color:var(--green-dark)}
.avatar{width:86px;height:86px;border-radius:50%;border:3px solid #3a3536;background:linear-gradient(160deg,#d9d9dd,#7b7f8a)}
.quote{width:255px;height:102px;background:var(--white);padding:14px 22px 0 27px;font-size:10.4px;line-height:13.6px;text-align:justify;color:#555}
.quote::before{content:"";position:absolute;left:-18px;top:26px;border:9px solid transparent;border-right-color:var(--white)}
.quote .q{position:absolute;font-size:34px;line-height:1;font-weight:900;color:#bbb;font-family:Georgia,serif}
.quote .q.open{left:5px;top:4px}
.quote .q.close{right:5px;bottom:-8px}
.site-footer{left:0;top:1157px;width:1024px;height:43px;background:var(--black);color:var(--white);font-style:italic;font-weight:700;font-size:14px;display:flex;align-items:center;justify-content:center}
</style>
</head>
<body>
<header class="site-header abs">
  <div class="brand abs"><span class="brand-name">Sidework Hub</span></div>
  <nav class="main-nav abs"><a class="active">Home</a><a>About Us</a><a>Services</a><a>Testimonial</a><a>Contact Us</a></nav>
</header>

<section class="hero abs"></section>
<h1 class="hero-title abs">Sidework Hub</h1>
<p class="hero-text abs">Lorem Ipsum is simply dummy text of the printing and typesetting industry. Lorem Ipsum has been the industry's standard dummy text ever since the 1500s, when an unknown printer took a galley of type and scrambled it to make a type specimen book.</p>
<div class="cta abs">Get Stared Now</div>
<div class="video abs">
  <div class="video-screen" role="img" aria-label="Video still of a man in a suit seated under desk lamps">
    <div class="video-bar"><div class="video-progress"><span></span></div>
      <svg width="12" height="12" style="position:absolute;left:14px;top:5px"><rect x="2" y="2" width="2.5" height="8" fill="#ccc"/><rect x="7" y="2" width="2.5" height="8" fill="#ccc"/></svg>
    </div>
  </div>
</div>
<div class="slide-arrow abs" style="left:0"><svg width="14" height="12" viewBox="0 0 14 12" fill="none" stroke="currentColor" stroke-width="2"><path d="M7 1 2 6l5 5M12 1 7 6l5 5"/></svg></div>
<div class="slide-arrow abs" style="left:988px"><svg width="14" height="12" viewBox="0 0 14 12" fill="none" stroke="currentColor" stroke-width="2"><path d="M2 1l5 5-5 5M7 1l5 5-5 5"/></svg></div>

<div class="benefit abs" style="left:135px">
  <div class="benefit-icon"><svg width="46" height="42" viewBox="0 0 46 42" fill="#fff"><path d="M18 4h10l5 8 4-2-3 11-11-2 4-2-4-7-4 7-6-3z"/><path d="M6 24l5-8 6 3-4 7h8v-4l7 9-7 9v-4H10z"/><path d="M40 24l-5-8-6 3 4 7 2 5h-2l0 0 3 9 4-6z"/></svg></div>
  <h3>LOREM IPSUM IS SIMPLY</h3>
  <p>Dummy text of the printing and typesetting industry. Lorem Ipsum has been the industry's standard dummy text ever since the 1500s,</p>
  <span class="btn">Read More</span>
</div>
<div class="benefit abs" style="left:327px">
  <div class="benefit-icon"><svg width="32" height="40" viewBox="0 0 32 40"><path d="M8 18V11a8 8 0 0 1 16 0v2" fill="none" stroke="#fff" stroke-width="5"/><rect x="2" y="18" width="28" height="20" rx="2" fill="#fff"/></svg></div>
  <h3>LOREM IPSUM IS SIMPLY</h3>
  <p>Dummy text of the printing and typesetting industry. Lorem Ipsum has been the industry's standard dummy text ever since the 1500s,</p>
  <span class="btn">Read More</span>
</div>
<div class="benefit abs" style="left:519px">
  <div class="benefit-icon"><svg width="50" height="44" viewBox="0 0 50 44" fill="#fff"><circle cx="10" cy="9" r="6"/><circle cx="40" cy="9" r="6"/><circle cx="25" cy="13" r="8"/><path d="M0 28a10 8 0 0 1 20 0v4H0zM30 28a10 8 0 0 1 20 0v4H30z"/><path d="M11 42a14 12 0 0 1 28 0v2H11z"/></svg></div>
  <h3>LOREM IPSUM IS SIMPLY</h3>
  <p>Dummy text of the printing and typesetting industry. Lorem Ipsum has been the industry's standard dummy text ever since the 1500s,</p>
  <span class="btn">Read More</span>
</div>
<form class="signup abs" style="left:711px">
  <h3>Free Consultion Signup</h3>
  <div class="field">Your Name</div>
  <div class="field">Email Address</div>
  <div class="field">Company Name</div>
  <div class="field">Phone</div>
  <span class="btn">Submit</span>
</form>

<section class="reviews abs"></section>
<h2 class="reviews-title abs">What Our Customers Have To Say</h2>

<div class="reviewer abs" style="left:137px;top:843px"><b>Aron Feldkamp</b> - Director Of Company Name</div>
<div class="avatar abs" style="left:137px;top:870px" role="img" aria-label="Portrait of a senior businessman"></div>
<div class="quote abs" style="left:248px;top:872px"><span class="q open">&ldquo;</span>When an unknown printer took a galley of type and scrambled it to make a type specimen book. It has survived not only five centuries, but also the leap into electronic typesetting<span class="q close">&rdquo;</span></div>

<div class="reviewer abs" style="left:521px;top:843px"><b>Jamie Morlan</b> - Director Of Company Name</div>
<div class="avatar abs" style="left:521px;top:870px" role="img" aria-label="Portrait of a smiling young man"></div>
<div class="quote abs" style="left:632px;top:872px"><span class="q open">&ldquo;</span>When an unknown printer took a galley of type and scrambled it to make a type specimen book. It has survived not only five centuries, but also the leap into electronic typesetting<span class="q close">&rdquo;</span></div>

<div class="reviewer abs" style="left:137px;top:996px"><b>Aron Feldkamp</b> - Director Of Company Name</div>
<div class="avatar abs" style="left:137px;top:1023px" role="img" aria-label="Portrait of a senior businessman"></div>
<div class="quote abs" style="left:248px;top:1025px"><span class="q open">&ldquo;</span>When an unknown printer took a galley of type and scrambled it to make a type specimen book. It has survived not only five centuries, but also the leap into electronic typesetting<span class="q close">&rdquo;</span></div>

<div class="reviewer abs" style="left:521px;top:996px"><b>Jamie Morlan</b> - Director Of Company Name</div>
<div class="avatar abs" style="left:521px;top:1023px" role="img" aria-label="Portrait of a smiling young man"></div>
<div class="quote abs" style="left:632px;top:1025px"><span class="q open">&ldquo;</span>When an unknown printer took a galley of type and scrambled it to make a type specimen book. It has survived not only five centuries, but also the leap into electronic typesetting<span class="q close">&rdquo;</span></div>

<footer class="site-footer abs">Built Using the Pagemarlo Landing Page</footer>
</body>
</html>
```